"Slipwise Forms" Cartvane Add-on Market Banner

Hey Designers! I need a photoshop banner to feature our web application, for use in the Cartvane Add-on Market. See http://addons.cartvane-example.com for examples of the other apps and their designs.
The image should be 310px wide x 100px tall. Suggested colors should be taken from our homepage: http://shop.slipwiseforms-example.com/ and are also suggested below.
At minimum, the app banner must contain the name "Slipwise Forms".
The application itself provides people with printable customized Invoice, Packing Slips templates, so imagery should reflect that in some way. Perhaps a printer or document icon for imagery.
I prefer flat design, or simple design without too much clutter or small details.
Target Market(s)
Adults based in United States, UK and Australia.. aged 25-35 who run online e-commerce businesses through Cartvane.com
Industry/Entity Type
Printer
Requirements
Must have
- The words "Slipwise Forms".
Black background, grey and white details.
Nice to have
- illustration style images, in flat design style if possible.
I like this type of design style: http://gridloft-example.com/tour/overview/
Should not have
- Photo like images.
White background.

```html
<!DOCTYPE html>
<html lang="en">
<head>
<meta charset="utf-8">
<title>Slipwise Forms — Add-on Market Banner</title>
<link rel="stylesheet" href="https://fonts.googleapis.com/css2?family=Jost:wght@500;600&display=swap">
<style>
  :root {
    --page: #ffffff;
    --frame: #e6e7e8;
    --ink: #231f20;
    --white: #ffffff;
    --soft: #e6e7e8;
  }
  html, body {
    margin: 0;
    padding: 0;
    width: 1200px;
    height: 900px;
    overflow: hidden;
    background: var(--page);
  }
  .canvas {
    position: relative;
    width: 1200px;
    height: 900px;
  }
  .banner-frame {
    position: absolute;
    left: 51px;
    top: 256px;
    width: 1102px;
    height: 354px;
    background: var(--frame);
  }
  .banner {
    position: absolute;
    left: 18px;
    top: 17px;
    width: 1066px;
    height: 320px;
    background: var(--ink);
  }
  .title-box {
    position: absolute;
    left: 99px;
    top: 62px;
    width: 859px;
    height: 59px;
    border: 4px solid var(--white);
    display: flex;
    align-items: center;
    justify-content: center;
  }
  .title {
    margin: 0;
    font-family: "Jost", sans-serif;
    font-weight: 600;
    font-size: 46px;
    letter-spacing: 9px;
    padding-left: 9px;
    color: var(--white);
    text-transform: uppercase;
    line-height: 1;
  }
  .feature-icons {
    position: absolute;
    left: 0;
    top: 163px;
    width: 100%;
    height: 60px;
  }
  .tagline {
    position: absolute;
    left: 0;
    top: 238px;
    width: 100%;
    margin: 0;
    display: flex;
    justify-content: center;
    align-items: center;
    gap: 26px;
    font-family: "Jost", sans-serif;
    font-weight: 600;
    font-size: 26px;
    letter-spacing: 5.5px;
    color: var(--soft);
    text-transform: uppercase;
    line-height: 1;
  }
  .tagline .bracket {
    font-weight: 500;
    font-size: 30px;
    letter-spacing: 0;
  }
</style>
</head>
<body>
  <main class="canvas">
    <section class="banner-frame">
      <div class="banner">
        <div class="title-box">
          <h1 class="title">Slipwise Forms</h1>
        </div>

        <svg class="feature-icons" viewBox="0 0 1066 60" aria-hidden="true">
          <g fill="none" stroke="#e6e7e8" stroke-width="4">
            <circle cx="356" cy="30" r="26"/>
            <circle cx="533" cy="30" r="26"/>
            <circle cx="710" cy="30" r="26"/>
          </g>
          <!-- screen share -->
          <g class="icon-screen">
            <path d="M345 35 h-4 v-17 h30 v17 h-4" fill="none" stroke="#e6e7e8" stroke-width="3"/>
            <path d="M356 30 l8 10 h-16 z" fill="#e6e7e8"/>
          </g>
          <!-- printer -->
          <g class="icon-printer" fill="#e6e7e8">
            <rect x="526" y="14" width="14" height="9" rx="1" fill="none" stroke="#e6e7e8" stroke-width="3"/>
            <rect x="521" y="23" width="24" height="12" rx="2"/>
            <rect x="526" y="33" width="14" height="12" fill="#231f20" stroke="#e6e7e8" stroke-width="3"/>
            <rect x="529" y="38" width="6" height="1.6" fill="#e6e7e8"/>
          </g>
          <!-- copies -->
          <g class="icon-copies" fill="#e6e7e8">
            <rect x="702" y="16" width="19" height="21"/>
            <rect x="696" y="22" width="19" height="21" stroke="#231f20" stroke-width="2.5"/>
          </g>
        </svg>

        <p class="tagline">
          <span class="bracket">[</span>
          <span>Custom Documents Made Simple</span>
          <span class="bracket">]</span>
        </p>
      </div>
    </section>
  </main>
</body>
</html>
```